Velcor Prime Brochure for Chemicals Products

We need a bifold A3 brochure for the exhibition.
you can visit our company website (www.velcorprime.com) for more information about our company.
Company logo and color code attached.
The brochure should contain brief introduction of company, industries, product, and contact (address , telephone and email; joral.k@velcorprime.com)

Product Portfolio:
1. Intermediates
2. Plastics
3. Rubber
4. Additive
5. Fiber
Detail of each products portfolio are in the website. we would like to add product detail but you may help to design how to put it beautifully.

Target Market(s)

Our customers are factories in related industry.

Industry/Entity Type

Automotive, Paint, Electrical Appliance, Tyre and footwear, Textile, Animal Feed, Lubricant

Font styles to use
Sans Serif

Requirements
Must have
• Logo, Product Portfolio for different market.
Nice to have
• prefer curve design rather than rectangular

```html
<!DOCTYPE html>
<html lang="en">
<head>
<meta charset="UTF-8">
<title>Velcor Prime – Company Profile</title>
<link href="https://fonts.googleapis.com/css2?family=Poppins:wght@400;500;700;800&display=swap" rel="stylesheet">
<style>
  :root {
    --brand-blue: #1b8fd9;
    --band-blue: #daf1fc;
    --ink-dark: #3b3b3b;
    --ink-body: #1e1e1e;
    --lime: #abd022;
    --pellet-light: #bfe3ef;
    --pellet-mid: #8fcfe0;
    --skin: #d9a48e;
    --page: #ffffff;
  }
  * { margin: 0; padding: 0; box-sizing: border-box; }
  html, body { width: 849px; height: 1200px; overflow: hidden; background: var(--page); }
  .page {
    position: relative;
    width: 849px;
    height: 1200px;
    font-family: "Poppins", sans-serif;
    color: var(--ink-body);
    overflow: hidden;
  }
  .header-band {
    position: absolute;
    left: 58px; top: 38px;
    width: 785px; height: 27px;
    background: var(--band-blue);
  }
  .brand-tab {
    position: absolute;
    left: 58px; top: 38px;
    width: 145px; height: 27px;
    background: var(--brand-blue);
    border-radius: 3px;
    color: #fff;
    font-size: 15px;
    font-weight: 500;
    line-height: 27px;
    text-align: center;
  }
  .section-title {
    position: absolute;
    left: 58px; top: 122px;
    font-size: 55px;
    font-weight: 800;
    line-height: 66px;
    letter-spacing: 0.5px;
  }
  .section-title .line-dark { color: var(--ink-dark); display: block; }
  .section-title .line-blue { color: var(--brand-blue); display: block; }
  .intro {
    position: absolute;
    left: 60px; top: 298px;
    width: 739px;
    font-size: 16.4px;
    line-height: 31px;
    text-align: justify;
  }
  .visit {
    position: absolute;
    left: 60px; top: 545px;
    font-size: 16.4px;
    line-height: 31px;
  }
  .visit a { color: var(--brand-blue); text-decoration: none; }
  .feature-art {
    position: absolute;
    left: 0; top: 0;
  }
</style>
</head>
<body>
<div class="page">
  <div class="header-band"></div>
  <div class="brand-tab">Velcor Prime</div>

  <h1 class="section-title">
    <span class="line-dark">COMPANY</span>
    <span class="line-blue">PROFILE:</span>
  </h1>

  <p class="intro">Established since 2004, Velcor Prime is a specialties chemicals and polymer distribution company serving customers in various industries, including coating, adhesives, automotive, electrical appliances, construction, medicals, tyre and rubber, animal feed, and textiles. Our products range from chemical intermediates, engineering plastics, synthetics rubber, additives, fiber and our own tailored made products. At Velcor Prime, our dedicated team thrive on providing innovative solutions and unmatched service to customers.</p>

  <p class="visit">Visit <a href="#">www.velcorprime.com</a> to learn more.</p>

  <svg class="feature-art" width="849" height="1200" viewBox="0 0 849 1200">
    <defs>
      <linearGradient id="pelletTones" x1="0" y1="0" x2="1" y2="1">
        <stop offset="0" stop-color="var(--pellet-light)"/>
        <stop offset="0.45" stop-color="#c8b3a6"/>
        <stop offset="0.7" stop-color="var(--pellet-mid)"/>
        <stop offset="1" stop-color="var(--pellet-light)"/>
      </linearGradient>
    </defs>
    <path class="accent-curve" fill="var(--lime)"
      d="M175 648 L415 648 Q460 648 461 700 L461 730 L100 985 Q58 985 60 940 L128 688 Q138 648 175 648 Z"/>
    <path role="img" aria-label="Photo of a hand holding light blue plastic polymer pellets"
      fill="url(#pelletTones)"
      d="M215 706 L843 706 L843 1192 L45 1192 L165 745 Q175 706 215 706 Z"/>
  </svg>
</div>
</body>
</html>
```